RTV Photography Business Card Design

I would like a business card designed in the shape of a camera.
Would like to see various camera designs. Would like to see what the card looks like in different colors. Would like to see which logo looks better on the various camera designs so please show me some with the white logo and some with the black logo. If you need a different file formats please let me know.
Project Deadline Extended Reason: My grandfather passed away and dealing with funeral plans so need to extend deadline. Added Tuesday, March 1, 2016
Project Deadline Extended
Reason: I just got back from out of town. My grandfather's passing was the primary focus for me these past few weeks and the funeral is over so now I will concentrate on picking my business card design. I really appreciate each designer who has taken the time to submit a design. Your effort has not gone unnoticed. I look forward to seeing more amazing designs.
Industry/Entity Type
Business
Contact Information for Business Card
Wren
757-418-2096
https://www.facebook.com/rtvphotographyfreelance/
DoraWren@rtv-photography.example
Look and feel

```html
<!DOCTYPE html>
<html lang="en">
<head>
<meta charset="utf-8">
<title>RTV Photography Business Card</title>
<link rel="stylesheet" href="https://fonts.googleapis.com/css2?family=Cinzel:wght@400&family=Open+Sans:wght@400;700&display=swap">
<style>
  :root {
    --stage: #e9e6e1;
    --card-black: #0b0b0b;
    --card-sheen: #2a2a2a;
    --gold-light: #f3d98a;
    --gold: #d4ad45;
    --gold-deep: #a67c1f;
    --white: #f4f4f4;
    --muted: #d8d8d8;
  }
  * { box-sizing: border-box; margin: 0; padding: 0; }
  html, body { width: 1200px; height: 1062px; overflow: hidden; }
  body {
    background: var(--stage);
    font-family: "Open Sans", Arial, sans-serif;
    position: relative;
  }
  .card {
    position: absolute;
    width: 700px;
    height: 400px;
    left: 250px;
    border-radius: 6px;
    background: linear-gradient(160deg, var(--card-black) 0%, var(--card-sheen) 45%, var(--card-black) 100%);
    box-shadow: 0 10px 30px rgba(0,0,0,0.25);
    overflow: hidden;
  }
  .card--front { top: 70px; }
  .card--back { top: 560px; }

  .brand {
    position: absolute;
    display: flex;
    align-items: center;
    gap: 14px;
    font-family: "Cinzel", Georgia, serif;
    color: var(--gold);
    letter-spacing: 2px;
    white-space: nowrap;
  }
  .brand__dot {
    width: 56px; height: 56px;
    border-radius: 50%;
    background: linear-gradient(135deg, var(--gold-light), var(--gold) 55%, var(--gold-deep));
    flex: none;
  }
  .card--front .brand { left: 44px; bottom: 42px; font-size: 20px; }

  .contact-box {
    position: absolute;
    right: 40px; top: 50px;
    width: 290px; height: 220px;
    border: 2px solid var(--gold);
    border-radius: 14px;
    padding: 26px 26px;
    color: var(--white);
  }
  .contact-box__name { color: var(--gold); font-weight: 700; font-size: 22px; line-height: 1.15; }
  .contact-box__title { font-size: 16px; line-height: 1.2; margin-bottom: 20px; }
  .contact-list { list-style: none; font-size: 15px; }
  .contact-list li { display: flex; align-items: center; gap: 10px; margin-bottom: 9px; white-space: nowrap; }
  .contact-list svg { width: 14px; height: 14px; flex: none; }

  .back-frame {
    position: absolute;
    inset: 22px;
    border: 3px solid var(--muted);
    border-radius: 22px;
  }
  .back-mark {
    position: absolute;
    left: 70px; top: 60px;
    width: 200px; height: 200px;
    border-radius: 50%;
    background: linear-gradient(135deg, var(--white) 0%, var(--gold-light) 40%, var(--gold) 70%, var(--gold-deep) 100%);
  }
  .card--back .brand {
    right: 70px; bottom: 70px;
    font-size: 22px;
    color: var(--white);
  }
</style>
</head>
<body>
  <section class="card card--front" aria-label="Business card front">
    <div class="brand">
      <span class="brand__dot"></span>
      <span class="brand__name">RTV PHOTOGRAPHY</span>
    </div>
    <div class="contact-box">
      <p class="contact-box__name">Ansel Ward</p>
      <p class="contact-box__title">Manager</p>
      <ul class="contact-list">
        <li>
          <svg viewBox="0 0 16 16" aria-hidden="true"><path fill="#d4ad45" d="M3 1l3 3-1.5 2a9 9 0 0 0 5.5 5.5L12 10l3 3-2 2C7 15 1 9 1 3z"/></svg>
          555 014 2270
        </li>
        <li>
          <svg viewBox="0 0 16 16" aria-hidden="true"><circle cx="8" cy="8" r="6.5" fill="none" stroke="#d4ad45" stroke-width="1.5"/><path d="M1.5 8h13M8 1.5c-3 3.5-3 9.5 0 13M8 1.5c3 3.5 3 9.5 0 13" fill="none" stroke="#d4ad45" stroke-width="1.2"/></svg>
          www.anselward.example
        </li>
        <li>
          <svg viewBox="0 0 16 16" aria-hidden="true"><text x="8" y="13" text-anchor="middle" font-size="14" font-weight="700" fill="#d4ad45" font-family="Open Sans, Arial, sans-serif">@</text></svg>
          ansel@anselward.example
        </li>
      </ul>
    </div>
  </section>

  <section class="card card--back" aria-label="Business card back">
    <div class="back-frame"></div>
    <div class="back-mark"></div>
    <div class="brand">
      <span class="brand__name">RTV PHOTOGRAPHY</span>
    </div>
  </section>
</body>
</html>
```